website design for a new age Real Estate Security Business

We are launching a business in real estate which no body else is doing. We are going to use technology in terms of software and hardware to provide our services.

We are going to use Big Data, IOT etc.. for our services.

NOTE: We don't want to see Shiel or buildings etc.. that directly suggests Real estate or security on this design

Target Market(s)

India

Industry/Entity Type

Real Estate

Number of Pages Required

4 page

Font styles to use
Sans Serif
Other font styles liked:
• Use Google Fonts

Requirements
Must have
• Home Page should be trendy and colourful should give user confidence to subscribe to our service.
Nice to have
• Use Google fonts.
Should not have
• Design shouldnt have Shield or Buildings that directly suggests real estate or security.

```html
<!DOCTYPE html>
<html lang="en">
<head>
<meta charset="utf-8">
<title>PlotSentry</title>
<link href="https://fonts.googleapis.com/css2?family=Lato:wght@300;400;700;900&display=swap" rel="stylesheet">
<style>
:root{
  --navy:#0f2c4f;
  --ink:#1d2b3a;
  --blue:#1d6fb8;
  --sky:#2fa6dd;
  --cyan:#36b9e4;
  --cyan-lite:#7fd3ef;
  --doc:#1e5a94;
  --land:#2d8fd0;
  --grey:#6f7680;
  --line:#e4e8ec;
  --paper:#ffffff;
  --foot:#f3f5f7;
}
*{box-sizing:border-box;margin:0;padding:0}
html,body{width:1200px;height:2948px;overflow:hidden}
body{font-family:"Lato",sans-serif;color:var(--ink);background:var(--paper)}
.site{width:1200px;height:2948px;position:relative}

/* header */
.topbar{height:120px;display:flex;align-items:center;justify-content:space-between;padding:0 40px;position:relative}
.brand{font-size:40px;font-weight:400;color:var(--blue);letter-spacing:.5px}
.topbar .util{position:absolute;top:10px;right:40px;display:flex;gap:18px;align-items:center;font-size:15px;color:var(--grey)}
.search{width:220px;height:28px;border:1px solid var(--line);border-radius:3px;padding:0 10px;font-size:13px;color:#9aa3ad;display:flex;align-items:center}
.phone{display:flex;align-items:center;gap:6px;color:var(--blue)}
.nav{display:flex;gap:0;margin-top:34px}
.nav a{font-size:17px;font-weight:700;color:var(--ink);text-decoration:none;padding:10px 22px}
.nav a.active{border-bottom:3px solid var(--blue)}

/* hero */
.hero{height:480px;background:radial-gradient(ellipse at 70% 50%,#23507e 0%,#0d2642 55%,#06162a 100%);color:#fff;text-align:center;padding-top:110px}
.hero h1{font-size:64px;font-weight:900;letter-spacing:1px}
.hero p{font-size:20px;font-weight:700;margin-top:14px;line-height:1.4}
.hero p.sub{font-weight:400;font-size:18px;margin-top:6px}
.btn-light{display:inline-block;margin-top:32px;background:#fff;color:var(--ink);font-weight:700;font-size:17px;padding:14px 34px;border-radius:3px}

/* social */
.social{height:90px;display:flex;justify-content:center;align-items:center;gap:40px;border-bottom:1px solid var(--line)}
.social span{width:18px;height:18px;border-radius:50%;background:#c4ccd4}

/* welcome */
.welcome{height:510px;text-align:center;padding:50px 120px 0}
.title{font-size:48px;font-weight:900;color:var(--navy)}
.title em{font-style:normal;color:var(--sky)}
.welcome .lead{font-size:15px;color:var(--grey);line-height:1.6;margin-top:22px}
.features{display:flex;justify-content:center;gap:110px;margin-top:40px}
.feature{width:200px}
.feature svg{width:70px;height:70px}
.feature h3{font-size:20px;font-weight:700;margin-top:8px}
.feature p{font-size:14px;color:var(--grey);line-height:1.5;margin-top:6px}

/* products */
.products{height:560px;position:relative;color:#fff}
.products .bg{position:absolute;inset:0}
.product{position:absolute;top:0;height:560px;width:600px;display:flex;align-items:center;gap:30px;padding:0 50px}
.product.doc{left:0}
.product.land{left:600px;flex-direction:row-reverse;padding-left:10px}
.art{width:260px;height:280px;border-radius:6px}
.art.doc-art{background:linear-gradient(135deg,#4fb0e6,#1a4d7e)}
.art.land-art{background:linear-gradient(135deg,#f0f4f8,#7ab8e2)}
.product h2{font-size:46px;font-weight:900}
.product p{font-size:15px;line-height:1.55;opacity:.85;margin-top:12px;max-width:230px}
.price{font-size:44px;font-weight:300;margin-top:18px}
.price small{font-size:18px}
.btn-white{display:inline-block;margin-top:14px;background:#fff;color:var(--ink);font-weight:700;font-size:17px;padding:10px 22px}

/* pricing */
.pricing{height:490px;padding-top:60px;text-align:center}
.plans{display:flex;justify-content:center;gap:20px;margin-top:30px;align-items:flex-start}
.plan{width:330px;border:1px solid var(--line);padding-bottom:30px}
.plan .head{background:#eef0f2;padding:22px 0}
.plan h4{font-size:24px;font-weight:900}
.plan .amt{font-size:62px;font-weight:900;line-height:1.1}
.plan .amt sup{font-size:28px;vertical-align:super}
.plan .term{font-size:13px;color:var(--grey)}
.plan p{font-size:14px;color:var(--grey);line-height:1.55;padding:24px 34px 0}
.btn-outline{display:inline-block;margin-top:22px;border:2px solid var(--navy);color:var(--navy);font-weight:700;font-size:16px;padding:10px 24px}
.plan.featured{margin-top:-20px;background:var(--navy);color:#fff;border-color:var(--navy)}
.plan.featured .head{background:var(--navy)}
.plan.featured .term,.plan.featured p{color:#c6d3e2}
.plan.featured .btn-outline{background:#fff;border-color:#fff}

/* contact */
.contact{height:340px;background:var(--cyan);text-align:center;padding-top:40px;color:#fff}
.contact .title{color:#fff}
.contact .title em{color:var(--navy)}
.contact .intro{font-size:15px;margin-top:8px;opacity:.9}
.form{width:900px;margin:24px auto 0;display:grid;grid-template-columns:1fr 1fr 1fr;gap:14px}
.field{background:var(--cyan-lite);height:44px;text-align:left;padding:12px 14px;font-size:14px;color:#e9f8fd}
.field.msg{grid-column:1/4;height:84px}
.btn-submit{display:inline-block;margin-top:16px;background:#fff;color:var(--navy);font-weight:900;font-size:16px;padding:10px 46px}

/* footer */
.footer{height:300px;background:var(--paper);display:grid;grid-template-columns:290px 230px 330px 250px;gap:0;padding:50px 50px 0}
.footer h5{font-size:18px;font-weight:700;color:var(--blue);margin-bottom:14px}
.footer .brand{font-size:34px}
.footer p,.footer li{font-size:14px;color:var(--grey);line-height:1.9;list-style:none}
.dots{display:flex;gap:12px;margin-top:18px}
.dots span{width:40px;height:40px;border-radius:50%;background:var(--doc)}
.news{display:flex;gap:14px;margin-bottom:16px}
.news .thumb{width:56px;height:56px;border-radius:50%;background:#b9c4cf;flex:none}
.news p{line-height:1.5}
.news small{color:var(--sky);font-size:12px}
.bottom{height:48px;background:var(--navy);color:#c9d4e0;font-size:14px;text-align:center;line-height:48px}
</style>
</head>
<body>
<div class="site">

<header class="topbar">
  <div class="brand">PlotSentry</div>
  <div class="util">
    <div class="search">Search...</div>
    <div class="phone">
      <svg width="16" height="16" viewBox="0 0 24 24"><path fill="#1d6fb8" d="M6.6 10.8a15 15 0 0 0 6.6 6.6l2.2-2.2a1 1 0 0 1 1-.25 11 11 0 0 0 3.6.6 1 1 0 0 1 1 1V20a1 1 0 0 1-1 1A17 17 0 0 1 3 4a1 1 0 0 1 1-1h3.5a1 1 0 0 1 1 1c0 1.25.2 2.45.6 3.6a1 1 0 0 1-.25 1z"/></svg>
      555 010 2040
    </div>
  </div>
  <nav class="nav">
    <a class="active">Home</a><a>About Us</a><a>Services</a><a>Pricing</a><a>Contact Us</a>
  </nav>
</header>

<section class="hero" role="img" aria-label="Dark blue digital network of glowing nodes and lines">
  <h1>PLOTSENTRY</h1>
  <p>We do monitors data from different sources to keep a property safe from encroachment...</p>
  <p class="sub">Lorem Ipsum is simply dummy text of the printing and typesetting industry. Lorem<br>Ipsum has been the industry's standard dummy text ever since the 1500s.</p>
  <span class="btn-light">LEARN MORE</span>
</section>

<div class="social"><span></span><span></span><span></span><span></span><span></span></div>

<section class="welcome">
  <h2 class="title">Welcome To <em>PlotSentry</em></h2>
  <p class="lead">When an unknown printer took a galley of type and scrambled it to make a type specimen book. It has survived not only five centuries, but also the leap into electronic typesetting, remaining essentially unchanged. It was popularised in the 1960s with the release of Letraset sheets containing Lorem Ipsum passages, and more recently with desktop publishing software like Aldus PageMaker including versions of Lorem Ipsum.</p>
  <div class="features">
    <div class="feature">
      <svg viewBox="0 0 70 70"><ellipse cx="35" cy="16" rx="20" ry="7" fill="#1d6fb8"/><path d="M15 16v36c0 4 9 7 20 7s20-3 20-7V16c0 4-9 7-20 7s-20-3-20-7z" fill="#2fa6dd"/><path d="M15 34c0 4 9 7 20 7s20-3 20-7" stroke="#fff" stroke-width="2" fill="none"/></svg>
      <h3>Data</h3>
      <p>When an unknown printer took a galley of type and scrambled it to make a type specimen.</p>
    </div>
    <div class="feature">
      <svg viewBox="0 0 70 70"><rect x="10" y="40" width="10" height="20" fill="#2fa6dd"/><rect x="25" y="28" width="10" height="32" fill="#1d6fb8"/><rect x="40" y="34" width="10" height="26" fill="#2fa6dd"/><rect x="55" y="18" width="10" height="42" fill="#0f2c4f"/><path d="M8 30 28 16 44 24 64 8" stroke="#0f2c4f" stroke-width="3" fill="none"/></svg>
      <h3>Analysis</h3>
      <p>When an unknown printer took a galley of type and scrambled it to make a type specimen.</p>
    </div>
    <div class="feature">
      <svg viewBox="0 0 70 70"><path d="M35 6 50 30 44 30 44 56 26 56 26 30 20 30z" fill="#1d6fb8"/><path d="M26 58h18l-9 10z" fill="#2fa6dd"/></svg>
      <h3>Action</h3>
      <p>When an unknown printer took a galley of type and scrambled it to make a type specimen.</p>
    </div>
  </div>
</section>

<section class="products">
  <svg class="bg" width="1200" height="560" viewBox="0 0 1200 560"><polygon points="0,0 640,0 560,560 0,560" fill="#1e5a94"/><polygon points="640,0 1200,0 1200,560 560,560" fill="#2d8fd0"/></svg>
  <div class="product doc">
    <div class="art doc-art" role="img" aria-label="Illustration of a laptop with document folders"></div>
    <div>
      <h2>Doc Secure</h2>
      <p>Lorem Ipsum is simply dummy text of the printing and typesetting industry. Lorem Ipsum has been the industry's standard dummy text ever since the 1500s.</p>
      <div class="price">$99<small>/each</small></div>
      <span class="btn-white">ADD TO CART</span>
    </div>
  </div>
  <div class="product land">
    <div class="art land-art" role="img" aria-label="Illustration of a dashboard screen with data charts"></div>
    <div>
      <h2>Land Secure</h2>
      <p>Lorem Ipsum is simply dummy text of the printing and typesetting industry. Lorem Ipsum has been the industry's standard dummy text ever since the 1500s.</p>
      <div class="price">$99<small>/each</small></div>
      <span class="btn-white">ADD TO CART</span>
    </div>
  </div>
</section>

<section class="pricing">
  <h2 class="title">Our <em>Pricing</em></h2>
  <div class="plans">
    <div class="plan">
      <div class="head"><h4>ADVANCE</h4><div class="amt"><sup>$</sup>59</div><div class="term">30 Days Trial</div></div>
      <p>Lorem Ipsum is simply dummy text of the printing and typesetting industry. Lorem Ipsum is simply dummy text of the printing and typesetting industry.</p>
      <span class="btn-outline">PURCHASE NOW</span>
    </div>
    <div class="plan featured">
      <div class="head"><h4>ADVANCE</h4><div class="amt"><sup>$</sup>80</div><div class="term">30 Days Trial</div></div>
      <p>Lorem Ipsum is simply dummy text of the printing and typesetting industry. Lorem Ipsum is simply dummy text of the printing and typesetting industry.</p>
      <span class="btn-outline">PURCHASE NOW</span>
    </div>
    <div class="plan">
      <div class="head"><h4>ADVANCE</h4><div class="amt"><sup>$</sup>99</div><div class="term">30 Days Trial</div></div>
      <p>Lorem Ipsum is simply dummy text of the printing and typesetting industry. Lorem Ipsum is simply dummy text of the printing and typesetting industry.</p>
      <span class="btn-outline">PURCHASE NOW</span>
    </div>
  </div>
</section>

<section class="contact">
  <h2 class="title">Contact <em>Us</em></h2>
  <p class="intro">Get in touch and we'll get back to you as soon as we can. We look forward to hearing from you!</p>
  <div class="form">
    <div class="field">Name*</div><div class="field">Contact No*</div><div class="field">Email*</div>
    <div class="field msg">Message*</div>
  </div>
  <span class="btn-submit">SUBMIT</span>
</section>

<footer class="footer">
  <div>
    <div class="brand">PlotSentry</div>
    <p>Lorem Ipsum is simply dummy text of the printing and typesetting industry.</p>
    <div class="dots"><span></span><span></span><span></span></div>
  </div>
  <div>
    <h5>Quick Links</h5>
    <ul><li>Home</li><li>About Us</li><li>What We Do</li><li>Pricing</li><li>Services</li><li>Contact Us</li></ul>
  </div>
  <div>
    <h5>Latest News</h5>
    <div class="news"><div class="thumb" role="img" aria-label="News thumbnail"></div><p>Lorem Ipsum is simply dummy text the print<br><small>May, 2017</small></p></div>
    <div class="news"><div class="thumb" role="img" aria-label="News thumbnail"></div><p>Lorem Ipsum is simply dummy text the print<br><small>May, 2017</small></p></div>
  </div>
  <div>
    <h5>Contact Us</h5>
    <p>Lorem Ipsum dummy text<br>Location 654321</p>
    <p>555 010 2040</p>
    <p>hello@plotsentry.example</p>
  </div>
</footer>
<div class="bottom">© PlotSentry.example - 2017. All Rights Reserved.</div>

</div>
</body>
</html>
```